Company profile urgent

Hi, I had my designer fail to deliver and I am looking for urgent designers job. Needs to go to print tomorrow the latest. I need company profile designed and finished, I do have a start of the project but did not like the overall design as it was too simple and not something I would asking for. This needs to be a great job and we are willing to pay for the right job.

This is pretty much a folded brochure as you will see from the document that is attached. On the front side do not remove LOGO from the actual position as it must stay there for the purposes of the cover that is going over and it has a whole for the logo where it is. Also, the pages are set as it should be so do not change the order of the pages, only the design, feel and look. This is for a travel company needs to look expensive, upscale, vip and must have clean design.

Needs to be done:

.

Needs to be done:

1) Get the design more attractive and modern. Not looking for cheap but high quality material.
2) As you can see we are tryin to present 4 products in the brochure that we do and this will be a folded brochure.
3) Infographics, especially the table ''when to travel'' needs updates and more style
4) This design is very steril, we are looking for clean and modern design
5) On the front page add Company profile text somewhere and add any design on home page is welcome BUT logo must stay where is
6) Please send final print ready documents as well as editable so we can move the logo if needed as it must fit the whole on a brochure holder
7) Last page with contacts very poorly done by my designer, needs upgrade with maybe infographics for phone, email web etc... ideas welcome
8) if you need more photos at the end is link to photo bank

Ideas welcome! Again we need it fast and clean.

Photo bank:
https://files.orvenbox.example/f/q7Lm2Xa9Tz4Pb8Kd

Designes that we linked: https://layoutmarket.example/item/company-profile-square-brochure/48817203?s_rank=8
https://layoutmarket.example/item/company-profile_square/51390628?s_rank=32
https://layoutmarket.example/item/square-brochure/53704916?s_rank=52

This is our webiste so you get the feeling of the colors: www.selvotrips.example

Important: Do not change text, or change pages, everything is as it should be just needs upgradede design! Logo on the first page must stay on the position as is.

Photo bank:

Target Market(s)

We are travel supplier targeting travel agents and travel companies

Industry/Entity Type

Travel Industry

Font styles to use
Serif
Sans Serif

Requirements
Must have
• https://files.orvenbox.example/f/w3Hn6Rc1Ys5Qe2Jv
Nice to have
• Cool design: https://layoutmarket.example/item/business-solution-brochure-template/46182057?s_rank=3
• Cool design 2: https://layoutmarket.example/item/travel-agency-catalog-brochure/47269815?s_rank=6
Should not have
• Do not change the dimensions. You have the design attached, indd file. Needs work and update.

```html
<!DOCTYPE html>
<html lang="en">
<head>
<meta charset="utf-8">
<title>Selvo Trips Croatia – Company Profile</title>
<link href="https://fonts.googleapis.com/css2?family=Open+Sans:wght@400;600;700&family=Montserrat:wght@400;600;800&display=swap" rel="stylesheet">
<style>
:root{
  --red:#a3172d;
  --red-dark:#8a1226;
  --red-soft:#c9405a;
  --red-map:#b3243a;
  --pink:#f6c3c8;
  --grey:#e8e6e6;
  --white:#ffffff;
}
*{margin:0;padding:0;box-sizing:border-box}
html,body{width:1200px;height:848px;overflow:hidden;background:#fff}
.board{position:relative;width:1130px;height:799px;transform:scale(1.0619);transform-origin:0 0;font-family:"Open Sans",Arial,sans-serif}
.strip{position:absolute;left:48px;width:1027px;box-shadow:0 4px 8px rgba(0,0,0,.28)}
.strip--front{top:128px;height:207px}
.strip--back{top:458px;height:205px}
.panel{position:absolute;top:0;height:100%;overflow:hidden}
.photo{position:absolute;inset:0}
.panel-head{position:absolute;left:0;top:12px;padding:4px 8px;font-family:"Montserrat",Arial,sans-serif;font-weight:600;font-size:5.6px;line-height:1.3;letter-spacing:.2px;text-transform:uppercase;color:var(--pink);background:var(--red-dark);white-space:nowrap}
.body-copy{position:absolute;left:8px;right:8px;color:var(--white);font-size:3.5px;line-height:1.45;font-weight:700}
.body-copy p{margin-bottom:3px}
.body-copy ul{list-style:none}
.body-copy li{margin-bottom:3.2px;font-weight:600}
.red-panel{background:var(--red)}
.grey-panel{background:var(--grey)}
.section-title{position:absolute;font-family:"Montserrat",Arial,sans-serif;font-weight:600;font-size:6.2px;color:var(--red);letter-spacing:.3px;text-transform:uppercase;white-space:nowrap}
.red-copy{position:absolute;color:var(--red);font-size:3.6px;line-height:1.5;font-weight:700}
.red-copy p{margin-bottom:4px}
.values{position:absolute;left:10px;top:135px;display:flex;gap:14px}
.value{width:60px;color:var(--red);font-size:3px;line-height:1.4;font-weight:600}
.value svg{display:block;margin-left:6px;margin-bottom:6px}
.value h4{font-size:3.4px;font-weight:800;margin-bottom:2px;text-transform:uppercase}
.tint{position:absolute;top:0;bottom:0;left:0;width:97px;background:rgba(163,23,45,.55)}
.wordmark{position:absolute;font-family:"Montserrat",Arial,sans-serif;font-weight:800;color:var(--red);letter-spacing:1px;text-align:center;white-space:nowrap}
.contact{position:absolute;top:168px;font-size:3.4px;line-height:1.6;color:var(--red);font-weight:600}
.contact strong{font-weight:800}
.tiles{position:absolute;left:12px;display:flex;gap:2px}
.tile{width:47px;height:45px}
.tiles--bottom .tile{width:46px}
.facts{position:absolute;left:266px;top:64px;width:70px;font-size:3px;line-height:1.45;color:var(--red);font-weight:600}
.facts dt{float:left;clear:left;width:22px;font-weight:800}
.facts dd{margin-left:24px}
.country-map{position:absolute;left:340px;top:60px;width:60px;height:52px;border-radius:4px;background:linear-gradient(135deg,var(--red-map),var(--red))}
.season{position:absolute;left:266px;top:121px;border-collapse:collapse;font-size:2.6px;color:var(--red);font-weight:700}
.season th,.season td{border-top:.5px solid var(--red-soft);height:5.6px;padding:0 1px;text-align:center;width:8.6px}
.season th.label,.season td.label{width:20px;text-align:left}
.season tbody tr:nth-child(odd){background:rgba(163,23,45,.08)}
.dot{display:inline-block;width:3.6px;height:3.6px;border:.5px solid var(--red);border-radius:50%}
.dot.on{background:var(--red)}
</style>
</head>
<body>
<div class="board">

  <section class="strip strip--front">
    <div class="panel red-panel" style="left:0;width:106px">
      <h2 class="panel-head" style="top:0;right:0;padding:10px 8px 6px;background:var(--red-soft)">Customized trips<br>throughout Croatia<br>and Eastern Europe</h2>
      <div class="body-copy" style="top:46px">
        <p>We create exceptional, customized itineraries. We are front line team of local experts, many of whom call Croatia home and are wonderfully experienced in the destinations. We visit our clients often, so every proposal is shaped by their needs and by what we see ourselves on the road each season.</p>
        <ul>
          <li>Itineraries crafted to perfection for every guest</li>
          <li>Exclusive contracted guest houses and hotels</li>
          <li>Unforgettable excursions on land and sea</li>
          <li>Wide selection of handpicked boutique stays and villas</li>
          <li>Only leading on the ground partners and guides</li>
          <li>Licensed and fully insured team on duty</li>
          <li>Private transfers and chauffeur service</li>
          <li>Combined city and island touring</li>
          <li>Showcase tours across Croatia, Slovenia and Montenegro</li>
        </ul>
      </div>
    </div>

    <div class="panel" style="left:106px;width:206px">
      <div class="photo" role="img" aria-label="Photo of a walled old town on a rocky Adriatic coast at sunset" style="background:linear-gradient(160deg,#b97fae 0%,#d9a27a 28%,#9c6a4e 48%,#2c5d86 70%,#123b66 100%)"></div>
    </div>

    <div class="panel" style="left:312px;width:98px">
      <div class="photo" role="img" aria-label="Photo of a coastal town with a red overlay" style="background:linear-gradient(180deg,#8e2242 0%,#a3243e 45%,#8c2a52 100%)"></div>
      <h2 class="panel-head" style="top:12px;width:82px">Small group tours<br>to Croatia<br>and Eastern Europe</h2>
      <div class="body-copy" style="top:46px">
        <p>We work with our team of local destination group experts to develop the finest programs for groups of every size, our group specialists have all the experience to handle the needs of each traveller perfectly.</p>
        <ul>
          <li>Tailor made group routes and timing</li>
          <li>Special dining and wine venues</li>
          <li>Group meals and tastings</li>
          <li>Value for high season dates</li>
          <li>Comfortable coaches and drivers</li>
        </ul>
      </div>
    </div>

    <div class="panel grey-panel" style="left:410px;width:305px">
      <h2 class="section-title" style="left:12px;top:20px">About Selvo Trips Croatia</h2>
      <div class="red-copy" style="left:12px;right:14px;top:42px">
        <p>Since 2003, our team is working specifically on crafting the tours to show all the unique experiences in Croatia and beyond including Montenegro, Serbia, Bosnia and Herzegovina, Greece and Albania. Selvo Trips Croatia is fully family owned and what we offer goes well beyond a travel package, we want all travelers to feel part of our family. The company is focused on detailed personalized services for travelers that are demanding the ultimate level of service, using carefully hand selected partners, drivers and guides in each destination to ensure the optimal travel experience.</p>
        <p>Our mission is to always offer exclusive experiences not of the public eye that are preserved for the most discerning travelers to discover the authentic way of life in Croatia and Eastern Europe. We feel that testing and staying on top of the new trends on the destinations, offering unique and crafted activities is our obligation. If you are looking to have a partner that will help you provide experiences that can't be found online, we are the right partner for you.</p>
      </div>
      <div class="values">
        <div class="value">
          <svg width="20" height="20" viewBox="0 0 20 20" aria-hidden="true"><rect x="2" y="2" width="16" height="16" rx="3" fill="var(--red)"/><path d="M6 10l3 3 5-6" stroke="#fff" stroke-width="1.8" fill="none"/></svg>
          <h4>Reliability</h4>Over 15 years of experience with most demanding travel agencies.
        </div>
        <div class="value">
          <svg width="20" height="20" viewBox="0 0 20 20" aria-hidden="true"><path d="M10 2a6 6 0 0 1 6 6c0 5-6 10-6 10S4 13 4 8a6 6 0 0 1 6-6z" fill="var(--red)"/><circle cx="10" cy="8" r="2.2" fill="#fff"/></svg>
          <h4>Local experience</h4>Local team that knows every corner of the region.
        </div>
        <div class="value">
          <svg width="20" height="20" viewBox="0 0 20 20" aria-hidden="true"><rect x="1" y="2" width="18" height="16" rx="2" fill="var(--red)"/><text x="10" y="13" text-anchor="middle" font-family="Montserrat,Arial,sans-serif" font-weight="800" font-size="7" fill="#fff">VIP</text></svg>
          <h4>Exclusivity</h4>Access to experiences out of the public eye.
        </div>
        <div class="value">
          <svg width="20" height="20" viewBox="0 0 20 20" aria-hidden="true"><circle cx="6" cy="5" r="2.5" fill="var(--red)"/><circle cx="14" cy="5" r="2.5" fill="var(--red)"/><path d="M2 18v-6a4 4 0 0 1 8 0M10 12a4 4 0 0 1 8 0v6" fill="var(--red)"/></svg>
          <h4>Personal approach</h4>Each client gets one dedicated travel consultant.
        </div>
      </div>
    </div>

    <div class="panel" style="left:715px;width:205px">
      <div class="photo" role="img" aria-label="Photo of a white speedboat cutting across blue sea at sunset" style="background:linear-gradient(100deg,#c97a5c 0%,#e4a986 30%,#f0e2d8 55%,#5d83a3 75%,#24496b 100%)"></div>
      <div class="tint"></div>
      <h2 class="panel-head" style="width:97px;padding:8px">Yachting</h2>
      <div class="body-copy" style="top:44px;width:84px">
        <p>Our yachting department has extensive knowledge of the Adriatic coast and all the destinations so we are able to create the optimal customized routes. Choose between 200 premium vessels, available for private or group charters across the coast.</p>
        <ul>
          <li>Private luxury yachts</li>
          <li>Catamarans</li>
          <li>Sailboats</li>
          <li>Motor yachts</li>
          <li>Gulets</li>
          <li>Mega yachts</li>
        </ul>
      </div>
    </div>

    <div class="panel red-panel" style="left:920px;width:107px">
      <h2 class="panel-head" style="top:12px;right:0;background:var(--red-soft);text-transform:none">SAVOURICA<br>The art of Croatian Gourmet</h2>
      <div class="body-copy" style="top:44px">
        <p>When it comes to culinary, it takes a blend of adventure, a dash of creativity and a resident expert to the ultimate local gourmet experiences. Savourica is our special department that works with local chefs, farms, wineries and markets to offer genuine tasting programs in every region of Croatia.</p>
        <ul>
          <li>Cooking classes with local chefs</li>
          <li>Truffle hunting in the hills</li>
          <li>Olive oil and wine tastings</li>
          <li>Oyster farm visits</li>
        </ul>
      </div>
    </div>
  </section>

  <section class="strip strip--back">
    <div class="panel" style="left:0;width:106px;background:linear-gradient(180deg,#b8475a,#a63a4f)">
      <h2 class="panel-head" style="top:12px;background:none;color:#fff;font-size:6.2px;text-transform:none">TRAVEL AGENTS,<br>what's in it for YOU?</h2>
      <div class="body-copy" style="top:38px">
        <ul>
          <li>We work exclusively with travel agents, we do not market or sell directly to the public.</li>
          <li>High paying commission up to 12%</li>
          <li>Incentive programs available</li>
          <li>Travel agent support and fast itinerary turnaround</li>
          <li>We are your strongest local link in Croatia and Eastern Europe</li>
        </ul>
      </div>
    </div>
    <div class="panel" style="left:106px;width:99px">
      <div class="photo" role="img" aria-label="Photo of a smiling travel consultant on the phone at her desk" style="background:linear-gradient(180deg,#c9b8a4 0%,#e7dcd2 45%,#d3c2b4 100%)"></div>
    </div>
    <div class="panel grey-panel" style="left:205px;width:205px">
      <div class="wordmark" style="left:0;right:0;top:104px;font-size:11px">SELVO TRIPS</div>
      <div class="contact" style="left:10px"><strong>SELVO TRIPS CROATIA</strong><br>12 Lindara Street, 10000 Zagreb<br>TEL: +385 1 555 0142<br>MOB: +385 91 555 0178</div>
      <div class="contact" style="left:152px">info@selvotrips.example<br><br>www.selvotrips.example</div>
    </div>
    <div class="panel grey-panel" style="left:410px;width:410px">
      <div class="tiles" style="top:12px">
        <div class="tile" role="img" aria-label="Photo of a stone church square" style="background:linear-gradient(#c6b59a,#8a7a63)"></div>
        <div class="tile" role="img" aria-label="Photo of a harbour town" style="background:linear-gradient(#8fb3d1,#b99a78)"></div>
        <div class="tile" role="img" aria-label="Photo of a sailboat at dusk" style="background:linear-gradient(#3b2b24,#c98b4c)"></div>
        <div class="tile" role="img" aria-label="Photo of a turquoise beach" style="background:linear-gradient(#8ed0e0,#e8dcc2)"></div>
        <div class="tile" role="img" aria-label="Photo of boats at a quay" style="background:linear-gradient(#6fa6c9,#c8a98c)"></div>
        <div class="tile" role="img" aria-label="Photo of a city cathedral" style="background:linear-gradient(#a9c6e0,#7d8d5f)"></div>
      </div>
      <h2 class="section-title" style="left:12px;top:82px;font-size:5.2px">Fully customized tours to Croatia and Eastern Europe</h2>
      <div class="red-copy" style="left:12px;width:240px;top:92px;font-size:3.4px">
        <p>Travel to Croatia and Eastern Europe crafted stress free. Experience the best of each destination as our passionate team of local experts plans the trip of your liking: unique accommodation, activities and sights only available for our travelers. From food and wine tours, active and soft adventure tours to culture and history tours, we can do it all and we do it with deep passion and love for our region. Every booking is equally important to us, get in touch and let us plan your next travel adventure.</p>
      </div>
      <dl class="facts">
        <dt>CURRENCY</dt><dd>Kuna (HRK)</dd>
        <dt>RELIGION</dt><dd>Catholic</dd>
        <dt>POPULATION</dt><dd>4.2 mil</dd>
        <dt>LANGUAGE</dt><dd>Croatian</dd>
        <dt>UNESCO</dt><dd>8 heritage sites</dd>
        <dt>PARKS</dt><dd>8 national, 11 nature</dd>
        <dt>AIRPORTS</dt><dd>Zagreb, Pula, Zadar, Split, Dubrovnik</dd>
      </dl>
      <div class="country-map" role="img" aria-label="Map of Croatia in red"></div>
      <table class="season">
        <thead><tr><th class="label"></th><th>JAN</th><th>FEB</th><th>MAR</th><th>APR</th><th>MAY</th><th>JUN</th><th>JUL</th><th>AUG</th><th>SEP</th><th>OCT</th><th>NOV</th><th>DEC</th></tr></thead>
        <tbody>
          <tr><td class="label">SIGHTSEEING</td><td><i class="dot"></i></td><td><i class="dot"></i></td><td><i class="dot on"></i></td><td><i class="dot on"></i></td><td><i class="dot on"></i></td><td><i class="dot on"></i></td><td><i class="dot on"></i></td><td><i class="dot on"></i></td><td><i class="dot on"></i></td><td><i class="dot on"></i></td><td><i class="dot"></i></td><td><i class="dot"></i></td></tr>
          <tr><td class="label">YACHTING</td><td><i class="dot"></i></td><td><i class="dot"></i></td><td><i class="dot"></i></td><td><i class="dot"></i></td><td><i class="dot on"></i></td><td><i class="dot on"></i></td><td><i class="dot on"></i></td><td><i class="dot on"></i></td><td><i class="dot on"></i></td><td><i class="dot"></i></td><td><i class="dot"></i></td><td><i class="dot"></i></td></tr>
          <tr><td class="label">FOOD</td><td><i class="dot on"></i></td><td><i class="dot on"></i></td><td><i class="dot on"></i></td><td><i class="dot on"></i></td><td><i class="dot on"></i></td><td><i class="dot on"></i></td><td><i class="dot on"></i></td><td><i class="dot on"></i></td><td><i class="dot on"></i></td><td><i class="dot on"></i></td><td><i class="dot on"></i></td><td><i class="dot on"></i></td></tr>
        </tbody>
      </table>
      <div class="tiles tiles--bottom" style="top:149px">
        <div class="tile" role="img" aria-label="Photo of a folk festival" style="background:linear-gradient(#5a3a2a,#b0764a)"></div>
        <div class="tile" role="img" aria-label="Photo of an old town street" style="background:linear-gradient(#9b8a78,#54483c)"></div>
        <div class="tile" role="img" aria-label="Photo of seafood dish" style="background:linear-gradient(#c2683c,#7a2f1c)"></div>
        <div class="tile" role="img" aria-label="Photo of a palace interior" style="background:linear-gradient(#c8a672,#7a5a36)"></div>
        <div class="tile" role="img" aria-label="Photo of islands from above" style="background:linear-gradient(#4b86b8,#2c5a7d)"></div>
        <div class="tile" role="img" aria-label="Photo of a cable car over a city" style="background:linear-gradient(#8fb5d5,#c88e5a)"></div>
        <div class="tile" role="img" aria-label="Photo of oranges on a branch" style="background:linear-gradient(#5c7a3a,#e59a2d)"></div>
        <div class="tile" role="img" aria-label="Photo of a couple in traditional costume" style="background:linear-gradient(#d8c7b0,#9b2a2a)"></div>
      </div>
    </div>
    <div class="panel" style="left:820px;width:207px">
      <div class="photo" role="img" aria-label="Photo of a marina below a walled town at sunset" style="background:linear-gradient(180deg,#7d5a86 0%,#d77a6c 30%,#efa26a 48%,#7a6e86 62%,#2f4a6b 80%,#1e3450 100%)"></div>
      <div class="wordmark" style="left:0;right:0;top:50px;font-size:13px">SELVO TRIPS</div>
    </div>
  </section>
</div>
</body>
</html>
```